Wedding Vow Design for Modern Print - SUBWAY PRINT STYLE or Similar, MODERN

I recently got married and I want to take the main words from my wedding vows and create a design using them that I can have printed and present to my new wife. I told her that I had privileges with Marring her and I made her promises. I would like to highlight both. We have a modern home and I want something that we can have professionally framed and hung on the wall. Love modern and clean design but something interesting.

Target Market(s)

Myself. 35, modern and loves clean design.

Industry/Entity Type

Wedding

Font styles to use
Serif

Colors
f6f3f8
ffffff
fbd4d5
000000
9d9d9d
dddddd

Requirements
Must have
• Cool, clean and modern design. Neutral Colors, Clean lines, Black and White, no reds, pinks, etc.
• We will hang this in our California modern home.
Nice to have
• Our wedding colors were , Gray,Black, Light Pink. I love the Subway signs and also love Black and White Word art.
Should not have
• Flowers, squiggly lines, traditional design. Something that would look great in a stainless metal frame or mirrored frame on white walls.

```html
<!DOCTYPE html>
<html lang="en">
<head>
<meta charset="UTF-8">
<title>Privileges &amp; Promises</title>
<link rel="stylesheet" href="https://fonts.googleapis.com/css2?family=Germania+One&family=Jost:wght@300;400&display=swap">
<style>
  :root {
    --paper: #d8b4b5;
    --paper-light: #dfbfc0;
    --paper-dark: #cfa8aa;
    --ampersand: rgba(140, 140, 140, 0.55);
    --headline: #ffffff;
    --word: #5a5456;
  }
  html, body {
    margin: 0;
    padding: 0;
    width: 900px;
    height: 1200px;
    overflow: hidden;
  }
  .vow-print {
    position: relative;
    width: 900px;
    height: 1200px;
    overflow: hidden;
    background:
      radial-gradient(circle at 20% 15%, var(--paper-light) 0%, transparent 45%),
      radial-gradient(circle at 80% 85%, var(--paper-dark) 0%, transparent 50%),
      var(--paper);
  }
  .artwork {
    position: absolute;
    inset: 0;
  }
  .ampersand {
    font-family: "Jost", sans-serif;
    font-weight: 400;
    fill: var(--ampersand);
  }
  .headline {
    font-family: "Germania One", serif;
    fill: var(--headline);
  }
  .word-list {
    position: absolute;
    margin: 0;
    padding: 0;
    list-style: none;
    font-family: "Jost", sans-serif;
    font-weight: 300;
    font-size: 32px;
    line-height: 70px;
    color: var(--word);
    letter-spacing: 0.2px;
  }
  .word-list--privileges {
    left: 229px;
    top: 120px;
  }
  .word-list--promises {
    right: 180px;
    top: 578px;
    text-align: right;
  }
</style>
</head>
<body>
<main class="vow-print">
  <svg class="artwork" width="900" height="1200" viewBox="0 0 900 1200" aria-hidden="true">
    <text class="ampersand" x="430" y="1010" font-size="1080" text-anchor="middle">&amp;</text>
    <text class="headline" transform="translate(222 973) rotate(-90)" font-size="165"
          textLength="866" lengthAdjust="spacingAndGlyphs">privileges</text>
    <text class="headline" transform="translate(846 1114) rotate(-90)" font-size="165"
          textLength="860" lengthAdjust="spacingAndGlyphs">promises</text>
  </svg>

  <ul class="word-list word-list--privileges" aria-label="Privileges">
    <li>Rest of My Life</li>
    <li>Protection</li>
    <li>Provision</li>
    <li>Love – Regardless</li>
    <li>Care</li>
    <li>Purpose</li>
    <li>Patience</li>
  </ul>

  <ul class="word-list word-list--promises" aria-label="Promises">
    <li>Fight</li>
    <li>Safety</li>
    <li>Cherish</li>
    <li>Unconditional Support</li>
    <li>Listen</li>
    <li>By Your Side</li>
    <li>The Best In You</li>
    <li>The Best In Me</li>
  </ul>
</main>
</body>
</html>
```